New to ArtHarbor? This contest is for you!

Are you new to ArtHarbor and looking to enter your first contest? Look no further!

We're launching this special contest to help you get started on building a design portfolio at ArtHarbor!

Requirements:
Create a mini one-page portfolio featuring selection of 3-5 designs from your personal portfolio to sell yourself as a designer.

The submission (1 page portfolio) should showcase your design skills to our design quality team and to our designers.

We've mocked up a few layouts to provide a guide for how to layout your submission. Please see the attachments to the brief. (This is a guide only.)

The mini portfolio should grab attention and communicate who your personal design brand.

Designers are limited to 1 design submission, so show us your best work!

You must upload your entry before 12:00am 1 Oct 2016 UTC

This must be your very FIRST entry on ArtHarbor to be eligible to receive a prize. If you've already entered other ArtHarbor contests you won't be eligible to win the prizes.

Your design must adhere to our quality standards and be approved by our quality team to be eligible to receive a prize.

Target Market(s)

ArtHarbor quality team
ArtHarbor customers

Industry/Entity Type

Graphic Design

Requirements
Must have
• Showcase 3-5 of your best designs from your personal work on 1 page.
• The portfolio should grab our judges attention and communicate who you are as a designer.
Nice to have
• Text or descriptions about the work is optional
Should not have
• No individual design examples should be submitted.

```html
<!DOCTYPE html>
<html lang="en">
<head>
<meta charset="utf-8">
<title>Mini Portfolio</title>
<link href="https://fonts.googleapis.com/css2?family=Open+Sans:wght@400;600;700&family=Montserrat:wght@600;700&display=swap" rel="stylesheet">
<style>
:root{
  --page:#ffffff;
  --panel:#f1f1f4;
  --v-red:#b3424b;
  --v-purple:#7c71a9;
  --v-green:#7fa44a;
  --v-teal:#5d9e91;
  --v-pink:#e0525e;
  --e-dark:#241a14;
  --e-wood:#5a3a22;
  --e-amber:#c98a2e;
  --t-ink:#222;
  --t-rose:#c9566a;
  --t-sky:#34a3d6;
  --t-navy:#2f3447;
  --s-navy:#1d3a66;
  --s-green:#7dbb3c;
  --text:#555;
}
*{box-sizing:border-box;margin:0;padding:0}
html,body{width:800px;height:1200px;overflow:hidden;background:var(--page);font-family:"Open Sans",sans-serif;color:var(--text)}
.canvas{position:relative;width:800px;height:1200px}
.panel{position:absolute;width:328px;height:486px;background:var(--panel)}
.site{position:absolute;overflow:hidden;background:#fff;font-size:3px;line-height:1.3}
.abs{position:absolute}
.photo{position:absolute}
.center{text-align:center}
.nav{position:absolute;display:flex;gap:4px;font-size:2.4px}
/* Vellum */
.vellum{left:141px;top:62px;width:153px;height:486px}
.vellum section{position:absolute;left:0;width:153px;color:#fff}
.v-logo{position:absolute;left:12px;top:4px;font-size:4px;font-weight:700;color:#fff}
.v-title{position:absolute;left:0;width:100%;text-align:center;font-size:5px;letter-spacing:.3px}
.v-sub{position:absolute;left:20px;width:113px;text-align:center;font-size:2.6px;opacity:.85}
.v-card{position:absolute;width:29px;height:42px;border:1px solid rgba(255,255,255,.4);background:rgba(255,255,255,.08);text-align:center;font-size:2.4px}
.v-card i{display:block;width:11px;height:11px;border-radius:50%;background:#fff;margin:5px auto 3px}
.v-member{position:absolute;width:29px;height:46px;background:rgba(0,0,0,.12);text-align:center;font-size:2.4px}
.v-member i{display:block;width:17px;height:17px;border-radius:50%;background:#e8e6f2;margin:5px auto 4px}
.v-thumb{position:absolute;width:32px;height:26px}
.v-btn{position:absolute;background:var(--v-green);color:#fff;font-size:2.4px;padding:1px 4px}
/* Ember */
.ember{left:516px;top:62px;width:134px;height:486px}
.e-label{position:absolute;border:1px solid #333;font-family:Montserrat,sans-serif;font-size:3px;font-weight:700;padding:1px 3px;color:#222}
.e-text{position:absolute;width:50px;font-size:2.4px;color:#777}
.e-banner{position:absolute;left:0;width:134px;color:#fff;font-family:Montserrat,sans-serif;font-weight:700;text-align:center;letter-spacing:.5px}
/* Thread */
.thread{left:154px;top:590px;width:128px;height:486px}
.t-prod{position:absolute;width:28px;height:36px;background:#eceef1}
.t-cap{position:absolute;width:28px;font-size:2.3px;text-align:center;color:#666}
/* Sentry */
.sentry{left:522px;top:590px;width:124px;height:486px}
.s-head{position:absolute;left:0;width:124px;text-align:center;font-size:3px;font-weight:700;color:#222}
.s-icon{position:absolute;width:9px;height:9px;border-radius:50%;background:var(--s-green)}
</style>
</head>
<body>
<div class="canvas">
  <div class="panel" style="left:54px;top:62px"></div>
  <div class="panel" style="left:420px;top:62px"></div>
  <div class="panel" style="left:54px;top:590px"></div>
  <div class="panel" style="left:420px;top:590px"></div>

  <!-- Vellum studio site -->
  <article class="site vellum">
    <section style="top:0;height:87px">
      <div class="photo" style="inset:0;background:linear-gradient(135deg,#7a5a44,#a98a6e 60%,#5f4634)" role="img" aria-label="Photo of a red notebook, flowers and a teapot on a wooden desk"></div>
      <div class="v-logo">Vellum</div>
      <div class="abs" style="left:58px;top:40px;font-size:3px;color:#eee">GOOD IDEA</div>
      <div class="abs" style="left:76px;top:37px;font-size:7px;font-weight:700;color:#5bc0eb">FIRST!</div>
      <div class="abs" style="left:14px;top:40px;font-size:6px;color:#fff">‹</div>
      <div class="abs" style="left:60px;top:72px;display:flex;gap:2px"><i style="width:2px;height:2px;background:#fff;border-radius:50%"></i><i style="width:2px;height:2px;background:#fff;border-radius:50%"></i><i style="width:2px;height:2px;background:#fff;border-radius:50%"></i><i style="width:2px;height:2px;background:#fff;border-radius:50%"></i></div>
    </section>
    <section style="top:87px;height:97px;background:var(--v-red)">
      <div class="v-logo">Vellum</div>
      <div class="nav" style="left:78px;top:4px"><span>Home</span><span>About</span><span>Work</span><span>Team</span><span>Contact</span></div>
      <div class="v-title" style="top:19px">OUR SERVICES</div>
      <div class="v-sub" style="top:29px">We design clear brands and simple sites</div>
      <div class="v-card" style="left:20px;top:45px"><i></i>Branding<br>Clean work</div>
      <div class="v-card" style="left:52px;top:45px"><i></i>Web<br>Clean work</div>
      <div class="v-card" style="left:84px;top:45px"><i></i>Print<br>Clean work</div>
      <div class="v-card" style="left:116px;top:45px"><i></i>Motion<br>Clean work</div>
    </section>
    <section style="top:184px;height:96px;background:var(--v-purple)">
      <div class="v-logo">Vellum</div>
      <div class="nav" style="left:78px;top:4px"><span>Home</span><span>About</span><span>Work</span><span>Team</span><span>Contact</span></div>
      <div class="v-title" style="top:17px">WHO WE ARE &amp; WHAT WE DO</div>
      <div class="v-sub" style="top:26px">A small studio with big ideas</div>
      <div class="v-btn" style="left:64px;top:33px">Meet the team</div>
      <div class="v-member" style="left:16px;top:43px"><i></i>Jane Cole</div>
      <div class="v-member" style="left:48px;top:43px"><i style="background:#e06a6a"></i>Jane Cole</div>
      <div class="v-member" style="left:80px;top:43px"><i></i>Jane Cole</div>
      <div class="v-member" style="left:112px;top:43px"><i></i>Jane Cole</div>
    </section>
    <section style="top:280px;height:110px;background:var(--v-green)">
      <div class="v-logo">Vellum</div>
      <div class="nav" style="left:78px;top:4px"><span>Home</span><span>About</span><span>Work</span><span>Team</span><span>Contact</span></div>
      <div class="v-title" style="top:17px">OUR WORK</div>
      <div class="nav" style="left:16px;top:34px;gap:14px"><span>All</span><span>Web</span><span style="background:#f0a030;padding:0 3px">Print</span><span>Brand</span></div>
      <div class="v-thumb" style="left:16px;top:44px;background:linear-gradient(#e9a55a,#4a3a30)" role="img" aria-label="Sunset landscape photo"></div>
      <div class="v-thumb" style="left:49px;top:44px;background:linear-gradient(#c7b89a,#3d3a38)" role="img" aria-label="Sunset landscape photo"></div>
      <div class="v-thumb" style="left:82px;top:44px;background:linear-gradient(#f0b060,#5a4030)" role="img" aria-label="Sunset landscape photo"></div>
      <div class="v-thumb" style="left:115px;top:44px;background:linear-gradient(#e8a040,#3a2a20)" role="img" aria-label="Sunset landscape photo"></div>
      <div class="v-thumb" style="left:16px;top:74px;background:linear-gradient(#d9c0a0,#4a3a30)" role="img" aria-label="Sunset landscape photo"></div>
      <div class="v-thumb" style="left:49px;top:74px;background:linear-gradient(#e9a55a,#3d3a38)" role="img" aria-label="Sunset landscape photo"></div>
      <div class="v-thumb" style="left:82px;top:74px;background:linear-gradient(#c7b89a,#5a4030)" role="img" aria-label="Sunset landscape photo"></div>
      <div class="v-thumb" style="left:115px;top:74px;background:linear-gradient(#f0b060,#3a2a20)" role="img" aria-label="Sunset landscape photo"></div>
    </section>
    <section style="top:390px;height:96px;background:var(--v-teal)">
      <div class="v-logo">Vellum</div>
      <div class="nav" style="left:78px;top:4px"><span>Home</span><span>About</span><span>Work</span><span>Team</span><span>Contact</span></div>
      <div class="v-title" style="top:17px">CONTACT US</div>
      <div class="abs" style="left:16px;top:42px;font-size:2.4px">Studio 4, Harbor Lane</div>
      <div class="photo" style="left:55px;top:40px;width:30px;height:26px;background:#e4e8e2" role="img" aria-label="Street map of the studio location"></div>
      <div class="abs" style="left:100px;top:40px;width:20px;height:5px;background:rgba(255,255,255,.3);font-size:2.3px;padding-left:1px">Name</div>
      <div class="abs" style="left:122px;top:40px;width:20px;height:5px;background:rgba(255,255,255,.3);font-size:2.3px;padding-left:1px">Email</div>
      <div class="abs" style="left:100px;top:47px;width:42px;height:14px;background:rgba(255,255,255,.3);font-size:2.3px;padding-left:1px">Message</div>
      <div class="abs" style="left:126px;top:64px;background:var(--v-pink);font-size:2.4px;padding:1px 4px">Send</div>
      <div class="abs" style="left:58px;top:84px;display:flex;gap:3px"><i style="width:7px;height:7px;border-radius:50%;background:rgba(255,255,255,.4)"></i><i style="width:7px;height:7px;border-radius:50%;background:rgba(255,255,255,.4)"></i><i style="width:7px;height:7px;border-radius:50%;background:rgba(255,255,255,.4)"></i><i style="width:7px;height:7px;border-radius:50%;background:rgba(255,255,255,.4)"></i></div>
    </section>
  </article>

  <!-- Ember grill site -->
  <article class="site ember">
    <div class="photo" style="left:0;top:0;width:134px;height:83px;background:radial-gradient(circle at 40% 60%,#8a4a22,#2a1a12 75%)" role="img" aria-label="Photo of grilled meat on a barbecue"></div>
    <div class="abs" style="left:0;top:0;width:134px;height:6px;background:rgba(0,0,0,.6)"></div>
    <div class="abs" style="left:3px;top:1px;font-size:3px;color:#fff;font-family:Montserrat,sans-serif">EMBER</div>
    <div class="nav" style="left:66px;top:1.5px;color:#ddd"><span>Home</span><span>Menu</span><span>Story</span><span>Visit</span></div>
    <div class="abs" style="left:42px;top:38px;border:1px solid #fff;padding:1px 4px;font-family:Montserrat,sans-serif;font-weight:700;font-size:10px;color:#fff;letter-spacing:1px">EMBER</div>
    <div class="abs center" style="left:0;top:56px;width:134px;font-size:2.4px;color:#ddd">Grill · Beer · Bread</div>

    <div class="e-label" style="left:22px;top:105px">OUR STORY</div>
    <div class="e-text" style="left:12px;top:117px">Slow fire, honest food and good company since day one.</div>
    <div class="photo" style="left:67px;top:91px;width:31px;height:30px;background:#7a3a1e" role="img" aria-label="Grilled chicken"></div>
    <div class="photo" style="left:99px;top:91px;width:31px;height:30px;background:#8a4a22" role="img" aria-label="Grilled ribs"></div>
    <div class="photo" style="left:67px;top:122px;width:31px;height:30px;background:#9a5a2a" role="img" aria-label="Roast potatoes"></div>
    <div class="photo" style="left:99px;top:122px;width:31px;height:30px;background:#6a2a1a" role="img" aria-label="Grilled skewers"></div>

    <div class="photo" style="left:0;top:156px;width:134px;height:67px;background:linear-gradient(90deg,#4a2e1a,#6a4428,#4a2e1a)" role="img" aria-label="Wooden wall with cured meat and wine"></div>
    <div class="e-banner" style="top:184px;font-size:7px">A SIMPLE CRAFT</div>

    <div class="photo" style="left:11px;top:233px;width:34px;height:56px;background:linear-gradient(#f5e6c0 15%,var(--e-amber) 30%,#7a4a18)" role="img" aria-label="Glass of beer"></div>
    <div class="e-label" style="left:84px;top:244px">OUR BEER</div>
    <div class="e-text" style="left:74px;top:256px">Brewed in house with local grain and hops.</div>

    <div class="photo" style="left:0;top:299px;width:134px;height:66px;background:linear-gradient(135deg,#3a2414,#8a5a2e,#3a2414)" role="img" aria-label="Loaves of bread and wheat"></div>
    <div class="e-banner" style="top:326px;font-size:7px">EARLY TO RISE</div>

    <div class="e-label" style="left:22px;top:383px">OUR BREAD</div>
    <div class="e-text" style="left:12px;top:395px">Baked fresh every morning before dawn.</div>
    <div class="photo" style="left:67px;top:375px;width:31px;height:64px;background:linear-gradient(#e8c37a,#a87a3a)" role="img" aria-label="Wheat stalks"></div>
    <div class="photo" style="left:99px;top:375px;width:31px;height:64px;background:linear-gradient(#d99a50,#b06a2a)" role="img" aria-label="Bread loaf"></div>

    <div class="abs" style="left:0;top:441px;width:134px;height:45px;background:var(--e-dark);color:#ddd;font-size:2.4px">
      <div class="abs center" style="left:0;top:6px;width:134px;color:var(--e-amber);font-size:3px">COME IN</div>
      <div class="abs center" style="left:0;top:11px;width:134px">Open daily from noon till late</div>
      <div class="abs" style="left:26px;top:24px;color:var(--e-amber)">CONNECT</div>
      <div class="abs" style="left:26px;top:29px;display:flex;gap:1.5px"><i style="width:4px;height:4px;border-radius:50%;background:#fff"></i><i style="width:4px;height:4px;border-radius:50%;background:#fff"></i><i style="width:4px;height:4px;border-radius:50%;background:#fff"></i><i style="width:4px;height:4px;border-radius:50%;background:#fff"></i></div>
      <div class="abs" style="left:96px;top:24px;color:var(--e-amber)">OR CALL</div>
      <div class="abs" style="left:94px;top:29px">000 555 0199</div>
    </div>
  </article>

  <!-- Thread & Co fashion store -->
  <article class="site thread">
    <div class="abs" style="left:0;top:2px;width:128px;font-size:2.2px;color:#777;padding-left:2px">Free shipping over $50</div>
    <div class="abs center" style="left:0;top:10px;width:128px;font-size:5px;font-weight:700;color:var(--t-ink)">Thread &amp; Co</div>
    <div class="abs" style="left:0;top:22px;width:128px;height:6px;border-top:1px solid #ddd;border-bottom:1px solid #ddd"></div>
    <div class="nav" style="left:10px;top:23px;gap:8px;color:#555"><span>Home</span><span>Women</span><span>Men</span><span>Shoes</span><span>Bags</span><span>Sale</span></div>
    <div class="photo" style="left:0;top:32px;width:128px;height:80px;background:linear-gradient(90deg,#6a625a,#b8b0a6 55%,#3a3634)" role="img" aria-label="Fashion model in a leather jacket on a city street"></div>
    <div class="photo" style="left:0;top:116px;width:41px;height:52px;background:linear-gradient(#9a9a9a,#444 60%,var(--t-rose) 60%)" role="img" aria-label="Black and white fashion photo"></div>
    <div class="photo" style="left:43px;top:116px;width:42px;height:52px;background:linear-gradient(#888,#333)" role="img" aria-label="Man in a suit"></div>
    <div class="photo" style="left:87px;top:116px;width:41px;height:52px;background:linear-gradient(#777,#222 60%,var(--t-sky) 60%)" role="img" aria-label="Handbag detail"></div>
    <div class="abs center" style="left:0;top:132px;width:41px;font-size:2.3px;color:#fff">NEW COLLECTION</div>
    <div class="abs center" style="left:0;top:157px;width:41px;font-size:2.3px;color:#fff">FREE SHIPPING</div>
    <div class="abs center" style="left:87px;top:157px;width:41px;font-size:2.3px;color:#fff">FREE RETURNS</div>
    <div class="abs" style="left:0;top:175px;width:128px;border-top:1px solid #333"></div>
    <div class="nav" style="left:40px;top:173px;background:#fff;padding:0 2px;color:#333"><span>Latest</span><span>Popular</span><span>Special</span></div>

    <div class="t-prod" style="left:4px;top:185px" role="img" aria-label="Model in summer outfit"></div>
    <div class="t-prod" style="left:36px;top:185px" role="img" aria-label="Model in summer outfit"></div>
    <div class="t-prod" style="left:68px;top:185px" role="img" aria-label="Model in summer outfit"></div>
    <div class="t-prod" style="left:100px;top:185px" role="img" aria-label="Model in summer outfit"></div>
    <div class="t-cap" style="left:4px;top:222px">Linen top<br>$29.00</div>
    <div class="t-cap" style="left:36px;top:222px">Linen top<br>$29.00</div>
    <div class="t-cap" style="left:68px;top:222px">Linen top<br>$29.00</div>
    <div class="t-cap" style="left:100px;top:222px">Linen top<br>$29.00</div>
    <div class="t-prod" style="left:4px;top:244px" role="img" aria-label="Model in summer outfit"></div>
    <div class="t-prod" style="left:36px;top:244px" role="img" aria-label="Model in summer outfit"></div>
    <div class="t-prod" style="left:68px;top:244px" role="img" aria-label="Model in summer outfit"></div>
    <div class="t-prod" style="left:100px;top:244px" role="img" aria-label="Model in summer outfit"></div>
    <div class="t-cap" style="left:4px;top:281px">Linen top<br>$29.00</div>
    <div class="t-cap" style="left:36px;top:281px">Linen top<br>$29.00</div>
    <div class="t-cap" style="left:68px;top:281px">Linen top<br>$29.00</div>
    <div class="t-cap" style="left:100px;top:281px">Linen top<br>$29.00</div>

    <div class="abs" style="left:4px;top:300px;font-size:2.4px;color:#333;font-weight:600">Style notes</div>
    <div class="abs" style="left:102px;top:300px;font-size:2.4px;color:#333;font-weight:600">NEWSLETTER</div>
    <div class="abs" style="left:102px;top:306px;width:22px;height:4px;border:1px solid #ccc"></div>

    <div class="photo" style="left:0;top:333px;width:64px;height:38px;background:linear-gradient(#e9c89a,#c89a6a)" role="img" aria-label="Woman in swimwear on a beach"></div>
    <div class="abs center" style="left:64px;top:333px;width:64px;height:38px;background:var(--t-navy);color:#fff;font-size:3px;padding-top:10px">SUMMER<br>COLLECTION<br><span style="font-size:2.3px">NOW IN STORE</span></div>

    <div class="abs" style="left:4px;top:380px;font-size:4px;color:#333">‹</div>
    <div class="abs" style="left:14px;top:378px;width:14px;height:10px;border-radius:50%;border:1px solid #999"></div>
    <div class="abs" style="left:38px;top:380px;font-size:4px;color:#333">Loomline</div>
    <div class="abs" style="left:70px;top:378px;width:11px;height:11px;background:#ccc"></div>
    <div class="abs" style="left:98px;top:378px;width:11px;height:11px;border-radius:50%;background:#ccc"></div>
    <div class="abs" style="left:122px;top:380px;font-size:4px;color:#333">›</div>

    <div class="abs" style="left:4px;top:396px;font-size:3.5px;font-weight:700;color:#222">Thread &amp; Co</div>
    <div class="abs" style="left:40px;top:396px;width:40px;font-size:2.3px;color:#666"><b>ABOUT US</b><br>Modern clothing for every day.</div>
    <div class="abs" style="left:96px;top:404px;display:flex;gap:1.5px"><i style="width:4px;height:4px;border-radius:50%;background:#222"></i><i style="width:4px;height:4px;border-radius:50%;background:#222"></i><i style="width:4px;height:4px;border-radius:50%;background:#222"></i><i style="width:4px;height:4px;border-radius:50%;background:#222"></i></div>
    <div class="abs" style="left:0;top:418px;width:128px;height:68px;background:#eeeeee"></div>
    <div class="nav" style="left:4px;top:424px;gap:14px;color:#333;font-weight:600"><span>Shop</span><span>Help</span><span>Account</span><span>Contact</span></div>
    <div class="abs center" style="left:0;top:460px;width:128px;font-size:2.2px;color:#888">© 2016 Thread &amp; Co</div>
    <div class="abs" style="left:0;top:481px;width:128px;height:1px;background:#333"></div>
  </article>

  <!-- SentryHut booth company -->
  <article class="site sentry">
    <div class="abs" style="left:46px;top:2px;font-size:3.5px;font-weight:700;color:var(--s-green)">SentryHut</div>
    <div class="abs" style="left:0;top:11px;width:124px;height:5px;background:var(--s-navy)"></div>
    <div class="nav" style="left:20px;top:11.5px;gap:7px;color:#fff"><span>Home</span><span>About</span><span>Services</span><span>Features</span><span>Contact</span></div>
    <div class="photo" style="left:0;top:16px;width:124px;height:70px;background:linear-gradient(#8ab0d8,#5a6a80 60%,#3a4250)" role="img" aria-label="Guard booth on a site under blue sky"></div>
    <div class="abs" style="left:48px;top:27px;width:64px;height:38px;background:var(--s-green);color:#fff;font-size:3px;font-weight:700;padding:3px">I HAVE A ___ AND WOULD LIKE TO KNOW MORE ABOUT SENTRYHUT BOOTHS</div>
    <div class="abs" style="left:70px;top:56px;background:var(--s-navy);color:#fff;font-size:2.2px;padding:1px 3px">Learn more</div>
    <div class="s-head" style="top:92px">ABOUT US</div>
    <div class="photo" style="left:10px;top:106px;width:48px;height:40px;background:linear-gradient(#9ab8d4,#4a5a6a)" role="img" aria-label="Guard booth photo"></div>
    <div class="abs" style="left:64px;top:108px;width:52px;font-size:2.4px"><b style="color:var(--s-green)">SENTRYHUT</b><br>Sturdy guard booths built to last.</div>
    <div class="abs" style="left:64px;top:125px;background:var(--s-navy);color:#fff;font-size:2.2px;padding:1px 3px">Learn more</div>
    <div class="abs" style="left:0;top:156px;width:124px;height:54px;background:var(--s-navy)"></div>
    <div class="s-head" style="top:160px;color:#fff">SERVICES</div>
    <div class="s-icon" style="left:11px;top:170px"></div>
    <div class="s-icon" style="left:40px;top:170px"></div>
    <div class="s-icon" style="left:71px;top:170px"></div>
    <div class="s-icon" style="left:101px;top:170px"></div>
    <div class="nav" style="left:8px;top:182px;gap:11px;color:#fff"><span>Custom Build</span><span>Delivery</span><span>Install</span><span>Support</span></div>
    <div class="s-head" style="top:212px">FEATURES</div>
    <div class="photo" style="left:0;top:225px;width:62px;height:48px;background:linear-gradient(#e8e8e8,#3a3a3a)" role="img" aria-label="Security guard with radio"></div>
    <div class="abs" style="left:62px;top:225px;width:62px;height:48px;background:var(--s-green);color:#fff;font-size:2.4px;padding:6px 4px">SENTRYHUT<br>Secure steel frame and clear glass.</div>
    <div class="abs" style="left:0;top:273px;width:62px;height:48px;background:var(--s-green);color:#fff;font-size:2.4px;padding:6px 4px">SENTRYHUT<br>Secure steel frame and clear glass.</div>
    <div class="photo" style="left:62px;top:273px;width:62px;height:48px;background:linear-gradient(#f2f2f2,#8a8a8a)" role="img" aria-label="Security cameras on a wall"></div>
    <div class="s-head" style="top:326px">TESTIMONIALS</div>
    <div class="abs center" style="left:20px;top:336px;width:84px;font-size:2.4px">Great booth, quick install and friendly team.</div>
    <div class="abs" style="left:15px;top:334px;font-size:5px;color:var(--s-green)">‹</div>
    <div class="abs" style="left:106px;top:334px;font-size:5px;color:var(--s-green)">›</div>
    <div class="abs" style="left:58px;top:350px;width:7px;height:7px;border-radius:50%;background:#bbb"></div>
    <div class="photo" style="left:0;top:370px;width:124px;height:50px;background:#e6e9e4" role="img" aria-label="Street map with office location"></div>
    <div class="abs" style="left:0;top:420px;width:124px;height:66px;background:var(--s-navy);color:#fff">
      <div class="abs" style="left:46px;top:5px;font-size:3.5px;font-weight:700">SentryHut</div>
      <div class="abs" style="left:30px;top:22px;width:6px;height:6px;border-radius:50%;background:var(--s-green)"></div>
      <div class="abs" style="left:59px;top:22px;width:6px;height:6px;border-radius:50%;background:var(--s-green)"></div>
      <div class="abs" style="left:88px;top:22px;width:6px;height:6px;border-radius:50%;background:var(--s-green)"></div>
      <div class="nav" style="left:29px;top:31px;gap:20px"><span>Call</span><span>Visit</span><span>Email</span></div>
      <div class="abs center" style="left:0;top:52px;width:124px;font-size:2.2px;opacity:.8">© 2016 SentryHut</div>
    </div>
  </article>
</div>
</body>
</html>
```